New business card for civil engineering company - "Keystone Audit"

We need a business card designed for our new structural engineering company.

The company name is "Keystone Audit" logo files attached.

We would like the following:
* Two-sided card
* Simple design

Information to be placed on the card:
Name - Marcus Dellow
Job Title - Director / Structural Engineer
Credentials - BEng(Hons), CPEng, CMengNZ, IntPE(NZ)
Email - marcus.dellow@keystoneaudit.co.nz
mobile - 0219364058
website - www.keystoneaudit.co.nz

```html
<!DOCTYPE html>
<html lang="en">
<head>
<meta charset="utf-8">
<title>Keystone Audit Business Card</title>
<link rel="stylesheet" href="https://fonts.googleapis.com/css2?family=Arimo:wght@400;700&display=swap">
<style>
  :root {
    --page: #ffffff;
    --card: #1f2426;
    --ink: #ffffff;
    --ink-soft: #dfe2e2;
  }
  html, body {
    margin: 0;
    padding: 0;
    width: 1200px;
    height: 1200px;
    overflow: hidden;
    background: var(--page);
    font-family: "Arimo", Arial, sans-serif;
  }
  .canvas {
    position: relative;
    width: 1200px;
    height: 1200px;
  }
  .card {
    position: absolute;
    left: 142px;
    background: var(--card);
    color: var(--ink);
  }
  .card--front {
    top: 42px;
    width: 921px;
    height: 526px;
    display: flex;
    align-items: center;
    justify-content: center;
  }
  .card--back {
    top: 616px;
    width: 925px;
    height: 528px;
  }
  .brand-name {
    margin: 0;
    font-weight: 400;
    color: var(--ink);
    text-transform: uppercase;
    white-space: nowrap;
  }
  .brand-name--front {
    font-size: 34px;
    letter-spacing: 5px;
  }
  .brand-name--back {
    position: absolute;
    left: 690px;
    top: 190px;
    font-size: 19px;
    letter-spacing: 3px;
  }
  .person-name {
    position: absolute;
    left: 56px;
    top: 94px;
    margin: 0;
    font-size: 56px;
    line-height: 1;
    font-weight: 700;
    letter-spacing: 3px;
  }
  .person-role,
  .person-credentials,
  .contact-line {
    position: absolute;
    left: 56px;
    margin: 0;
    font-weight: 700;
    letter-spacing: 2px;
    line-height: 1;
    white-space: nowrap;
  }
  .person-role { top: 164px; font-size: 24px; }
  .person-credentials { top: 205px; font-size: 24px; }
  .contact-line { font-size: 22px; color: var(--ink-soft); }
  .contact-line--email { top: 342px; }
  .contact-line--phone { top: 388px; }
  .contact-line--web { top: 433px; }
</style>
</head>
<body>
  <div class="canvas">
    <section class="card card--front">
      <p class="brand-name brand-name--front">Keystone Audit</p>
    </section>

    <section class="card card--back">
      <h1 class="person-name">Marcus Dellow</h1>
      <p class="person-role">Director/Structural Engineer</p>
      <p class="person-credentials">BEng(Hons),CPEng,CMengNZ,IntPE(NZ)</p>
      <p class="brand-name brand-name--back">Keystone Audit</p>
      <p class="contact-line contact-line--email">marcus.dellow@keystoneaudit.co.nz</p>
      <p class="contact-line contact-line--phone">0219364058</p>
      <p class="contact-line contact-line--web">www.keystoneaudit.co.nz</p>
    </section>
  </div>
</body>
</html>
```